Silver Harbors and Forgotten Lanterns needs and awesome cover!

Silver Harbors is a book that talks about the awesomeness and majesty of angelic encounters and reveals that people can experience this today. I would like a cover that portrays an angel looking handsome and powerful, serious but not mean, angelic... I really liked the cover for the glass orchard. The colors and presentation looked very much like what I would like to have for my angel book. (Rich colors)
This is for a print book,(6 x 9) and usually I have used my print cover for my e-book as well. The cover will be uploaded to brindle press , the publishing company of vornaleaf.com.
If you need any info or have questions feel free to ask and I will do my best.

OK SORRY FOR BEING UNCLEAR TO ALL OF YOU (my first time here)
The colors schemes I really like are rich bold colors. I like the rich browns and golds of Daniel Hartwick's book "The glass Orchard" I also like deep reds. I also like bold text. something even if elegant is powerful. Also, the kind of angels I like are serious and noble yet kind. Tobias Renvald has an excellent example in his work "Veilleur Bastien" (watchman Bastien)
There are a lot of covers out there about heaven and angels and there seems to be a lot of clouds and angel statues. I would like something bold that would compel someone to want these encounters for themselves.
IF you have any specific questions I will answer them. Thanks for your patience.

The title is in Spanish...
PUERTOS PLATEADOS
y Linternas Olvidadas
Vuelven al Alba

And my name is ... Gregory Ostrander

Thank you.

Target Market(s)

My readers are all pretty much people who embrace the supernatural things of God. Angels, miracles, signs and wonders etc..

Industry/Entity Type

Publishing Company

Font styles to use
Serif
Decorative

Requirements
Must have
• Bold text. whether plain or elegant.
Rich colors. not a fan of washed out colors for this topic. I like golds and browns and deep reds
Nice to have
• Would be nice to see an angel on the cover but not a requirement. The angel should actually look like one that someone would like to see. Powerful but not scary. like Tobias renvald's Bastien the watchman.

OK I don't want to stop anyone's creativity ... If you can covey that angelic encounters are awesome and amazing without using an angel, that is fine! I know there are many ways to accomplish that, not just one.

The original cover I did for the English version is still being used on vornaleaf.com, and it is really basic. I just want to get a cover that inspires.
Should not have
• nothing negative or demonic in symbols.
Female angels. I'm not against female angels but most of the angels I am aware of are male.
ANGELS SHOULD HAVE CLOTHES ON.

Inspiring photos now uploaded... Any image actually used, I will buy the usage rights for it.

```html
<!DOCTYPE html>
<html lang="es">
<head>
<meta charset="utf-8">
<title>Puertos Plateados — Cover Wrap</title>
<link rel="stylesheet" href="https://fonts.googleapis.com/css2?family=Cinzel:wght@400;700&family=EB+Garamond:ital,wght@1,400;1,500&display=swap">
<style>
:root{
  --sky-top:#c9a57a;
  --sky-mid:#8d6a4c;
  --sky-low:#3b2a20;
  --parchment-light:#ede3c6;
  --parchment-dark:#c9b285;
  --scroll-edge:#7a4a1c;
  --ink:#2a1a10;
  --crimson:#7d1414;
  --gold-light:#fff1d0;
  --gold:#f0c682;
  --gold-deep:#c98b45;
  --cream:#fbf0dc;
  --spine:#e6d7b6;
}
*{margin:0;padding:0;box-sizing:border-box}
html,body{width:1200px;height:874px;overflow:hidden;background:#000}
.cover{position:relative;width:1200px;height:874px;overflow:hidden;
  background:linear-gradient(180deg,var(--sky-top) 0%,#b48a60 35%,var(--sky-mid) 65%,var(--sky-low) 100%);}
.back-sky{position:absolute;left:0;top:0;width:562px;height:874px;
  background:radial-gradient(ellipse at 50% 30%,#e9d8bc 0%,#b7987a 45%,#5a4536 100%);}
.front-sky{position:absolute;left:640px;top:0;width:560px;height:874px;
  background:radial-gradient(ellipse at 70% 20%,#f4cf8c 0%,#c58a4e 35%,#6b4128 70%,#2d1a10 100%);}

/* back cover */
.top-rule{position:absolute;left:50px;top:34px;width:470px;height:12px}
.scroll-frame{position:absolute;left:55px;top:40px;width:475px;height:810px;border-radius:18px;
  background:linear-gradient(180deg,#b78a3c,var(--scroll-edge) 50%,#b78a3c);}
.parchment{position:absolute;left:80px;top:92px;width:430px;height:710px;border-radius:10px;
  background:radial-gradient(ellipse at 50% 40%,var(--parchment-light) 0%,#e0d1a8 70%,var(--parchment-dark) 100%);
  box-shadow:inset 0 0 18px rgba(90,60,20,.45);}
.back-copy{position:absolute;left:96px;top:118px;width:394px;text-align:center;color:var(--crimson)}
.back-title{font-family:"Cinzel",serif;font-weight:400;line-height:1}
.back-title .main{display:block;font-size:62px;letter-spacing:1px}
.back-title .second{display:block;font-size:34px;margin-top:6px}
.back-sub{font-family:"Cinzel",serif;font-size:14.5px;line-height:1.15;color:var(--ink);margin-top:6px}
.divider{display:block;width:190px;height:8px;margin:14px auto 10px}
.blurb{font-family:"EB Garamond",serif;font-style:italic;font-size:13.6px;line-height:20.5px;
  color:var(--ink);text-align:justify;}
.blurb p+p{margin-top:20px}
.back-author{font-family:"Cinzel",serif;font-size:29px;letter-spacing:.5px;margin-top:6px}

/* spine */
.spine{position:absolute;left:562px;top:0;width:78px;height:874px;
  background:linear-gradient(90deg,#cdb88e,var(--spine) 30%,var(--spine) 70%,#cdb88e);}
.spine-author,.spine-title{position:absolute;writing-mode:vertical-rl;font-family:"Cinzel",serif;font-weight:400;color:var(--crimson);white-space:nowrap}
.spine-author{left:26px;top:40px;font-size:21px;line-height:1}
.spine-art{position:absolute;left:14px;top:318px;width:52px;height:134px;border-radius:4px;
  background:linear-gradient(180deg,#8f8071 0%,#b3321e 45%,#8a1d12 100%)}
.spine-title{left:10px;top:466px;line-height:1}
.spine-title .main{display:block;font-size:35px}
.spine-title .sub{display:block;font-size:14.5px;margin-right:5px}

/* front */
.front-author{position:absolute;left:640px;top:52px;width:560px;text-align:center;
  font-family:"Cinzel",serif;font-weight:400;font-size:38px;color:var(--cream);letter-spacing:1px;
  text-shadow:0 2px 6px rgba(60,30,10,.6)}
.angel-art{position:absolute;left:730px;top:120px;width:460px;height:690px;
  border-radius:46% 46% 10% 10%/30% 30% 6% 6%;
  background:radial-gradient(ellipse at 35% 65%,#ffe9b0 0%,#d88a3e 18%,#8f2a18 45%,rgba(140,110,90,.85) 70%,rgba(120,90,70,0) 100%);}
.front-title{position:absolute;left:640px;top:596px;width:560px;text-align:center;font-family:"Cinzel",serif;font-weight:400;line-height:1}
.front-title .main,.front-title .second{display:block;
  background:linear-gradient(180deg,var(--gold-light) 0%,var(--gold) 55%,var(--gold-deep) 100%);
  -webkit-background-clip:text;background-clip:text;color:transparent;
  filter:drop-shadow(0 2px 3px rgba(40,15,5,.7))}
.front-title .main{font-size:98px}
.front-title .second{font-size:64px;margin-top:2px}
.front-sub{position:absolute;left:640px;top:794px;width:560px;text-align:center;
  font-family:"Cinzel",serif;font-weight:400;font-size:22px;line-height:28px;color:var(--cream);
  text-shadow:0 1px 4px rgba(0,0,0,.6)}
</style>
</head>
<body>
<div class="cover">
  <div class="back-sky"></div>
  <div class="front-sky"></div>

  <section class="back">
    <svg class="top-rule" viewBox="0 0 470 12" aria-hidden="true">
      <line x1="0" y1="6" x2="470" y2="6" stroke="#2a1a10" stroke-width="2"/>
    </svg>
    <div class="scroll-frame" role="img" aria-label="Ornate golden unfurled scroll frame"></div>
    <div class="parchment"></div>
    <div class="back-copy">
      <h2 class="back-title"><span class="main">PUERTOS</span><span class="second">PLATEADOS</span></h2>
      <p class="back-sub">Y Linternas Olvidadas<br>(Vuelven al Alba)</p>
      <svg class="divider" viewBox="0 0 190 8" aria-hidden="true"><line x1="0" y1="4" x2="190" y2="4" stroke="#8a6a3c" stroke-width="1.5"/><circle cx="95" cy="4" r="3" fill="#8a6a3c"/></svg>
      <div class="blurb">
        <p>Lorem Ipsum is simply dummy text of the printing and typesetting industry. Lorem Ipsum has been the industry's standard dummy text ever since the 1500s, when an unknown printer took a galley of type and scrambled it to make a type specimen book.</p>
        <p>It has survived not only five centuries, but also the leap into electronic typesetting, remaining essentially unchanged. It was popularised in the 1960s with the release of Typeline sheets containing Lorem Ipsum passages, and more recently with desktop publishing software like Corvane PageSetter including versions of Lorem Ipsum.</p>
        <p>Lorem Ipsum is simply dummy text of the printing and typesetting industry. Lorem Ipsum has been the industry's standard dummy text ever since the 1500s, when an unknown printer took a galley of type and scrambled it to make a type specimen book.</p>
      </div>
      <svg class="divider" viewBox="0 0 190 8" aria-hidden="true"><line x1="0" y1="4" x2="190" y2="4" stroke="#8a6a3c" stroke-width="1.5"/><circle cx="95" cy="4" r="3" fill="#8a6a3c"/></svg>
      <p class="back-author">Gregory Ostrander</p>
    </div>
  </section>

  <section class="spine">
    <p class="spine-author">Gregory Ostrander</p>
    <div class="spine-art" role="img" aria-label="Small figure of the armoured angel with shield"></div>
    <p class="spine-title"><span class="main">Puertos Plateados</span><span class="sub">y Linternas Olvidadas (Vuelven al Alba)</span></p>
  </section>

  <section class="front">
    <p class="front-author">Gregory Ostrander</p>
    <div class="angel-art" role="img" aria-label="Winged angel in red tunic leaning on a glowing shield, head bowed in thought"></div>
    <h1 class="front-title"><span class="main">PUERTOS</span><span class="second">PLATEADOS</span></h1>
    <p class="front-sub">Y Linternas Olvidadas<br>(Vuelven al Alba)</p>
  </section>
</div>
</body>
</html>
```